A Dedicated Thank You to my Dad

Proposed Dimensions: Approx. 20" x 30"

For Father's Day, I wrote a dedication to my Dad that encapsulates my gratitude for everything he does, and everything he is. His birthday is on August 3, but it is more important for me to transform this dedication into a meaningful and memorable gift than to meet any deadline. I would love an image that captures the relationship between a father and his son, accompanied by my words of thanks in some sort of font that is appropriate for the message (calligprahy? not sure about that).

I had actually posted the Thank You on Chatterloop as a public post, so anyone with an account can read it: https://www.chatterloop.example/photo.php?fbid=20473819265038417&set=a.918364027159.5829361.3940582&type=1&theater

Only the words starting with "Thank you ..." should be on the poster.

Target Market(s)

This is a personal gift for my Dad. He doesn't have the best of eyesight, so having the words in a really small font would not be particularly helpful. :-)

Requirements
Must have
• * Personable
* Warm
* Inviting
* Memorable
* Understated more favored over Loud
Should not have
• * An entire palette of colors
* Wacky colors or fonts

```html
<!DOCTYPE html>
<html lang="en">
<head>
<meta charset="utf-8">
<title>Thank you, Dad, for</title>
<link rel="stylesheet" href="https://fonts.googleapis.com/css2?family=Dancing+Script:wght@500;700&family=Open+Sans:wght@400&display=swap">
<style>
  :root {
    --backdrop: #ececec;
    --sky-top: #3f86c0;
    --sky-mid: #6eaed9;
    --sky-low: #a9d6ee;
    --title-blue: #1c7fd4;
    --body-ink: #25425c;
    --lesson-ink: #1d3550;
    --wave-blue: #1a78c8;
    --wave-light: #e8f4fb;
    --grass-dark: #4b4a2a;
    --grass-tan: #9b9468;
    --star: #ffffff;
  }
  * { margin: 0; padding: 0; box-sizing: border-box; }
  html, body {
    width: 923px; height: 1200px; overflow: hidden;
    background: var(--backdrop);
  }
  .poster-frame {
    position: absolute; left: 34px; top: 0;
    width: 657px; height: 922px;
    transform: scale(1.3015);
    transform-origin: top left;
  }
  .poster {
    position: relative; width: 100%; height: 100%; overflow: hidden;
    background: linear-gradient(180deg, var(--sky-top) 0%, var(--sky-mid) 45%, var(--sky-low) 78%, var(--sky-low) 100%);
  }
  .star {
    position: absolute; width: 3px; height: 3px; border-radius: 50%;
    background: var(--star); opacity: .9;
  }
  .title {
    position: absolute; top: 30px; left: 0; width: 100%;
    text-align: center;
    font-family: "Dancing Script", cursive;
    font-weight: 700; font-size: 52px; font-style: italic;
    color: var(--title-blue);
    -webkit-text-stroke: 1px #ffffff;
    text-shadow: 0 0 2px #fff, 0 0 1px #fff;
    letter-spacing: 1px;
  }
  .dedication {
    position: absolute; top: 131px; left: 0; width: 100%;
    text-align: center;
    font-family: "Open Sans", sans-serif;
    font-size: 11.4px; line-height: 19.6px;
    color: var(--body-ink);
  }
  .dot { color: var(--star); opacity: .8; font-size: 9px; padding: 0 2px; }
  .waves { position: absolute; left: 0; top: 480px; width: 657px; height: 130px; }
  .lesson {
    position: absolute; top: 522px; left: 42px;
    font-family: "Dancing Script", cursive;
    font-weight: 500; font-style: italic; font-size: 19px;
    color: var(--lesson-ink);
    transform: rotate(4.3deg); transform-origin: left center;
    white-space: nowrap; letter-spacing: .6px;
  }
  .photo-scene {
    position: absolute; left: 0; bottom: 0; width: 100%; height: 320px;
    background: linear-gradient(180deg, rgba(169,214,238,0) 0%, rgba(155,148,104,.35) 35%, var(--grass-tan) 62%, var(--grass-dark) 100%);
  }
</style>
</head>
<body>
  <div class="poster-frame">
    <main class="poster">
      <span class="star" style="left:20px;top:80px"></span>
      <span class="star" style="left:66px;top:100px"></span>
      <span class="star" style="left:396px;top:28px"></span>
      <span class="star" style="left:552px;top:142px"></span>
      <span class="star" style="left:600px;top:113px"></span>
      <span class="star" style="left:38px;top:168px"></span>
      <span class="star" style="left:116px;top:50px"></span>

      <h1 class="title">Thank you, Dad, for</h1>

      <p class="dedication">
        always carrying us to the car<br>
        after we fell asleep, even after we were definitely old<br>
        enough to walk it <span class="dot">•</span> welcoming more people to stay with us than<br>
        I can count <span class="dot">•</span> doggedly trying to teach me that the beach is not to be feared<br>
        nor cleaned <span class="dot">•</span> loading us all up in the station wagon, pillows in tow, so we could watch<br>
        the first drive-in movie together and squint in the second <span class="dot">•</span> as coach, letting me take a fake<br>
        rabbit's foot onto the soccer field <span class="dot">•</span> letting me sing in my room as if I were the originating artist <span class="dot">•</span><br>
        making car trips with you, wherever we were going, fun and special <span class="dot">•</span> putting up with the commutes<br>
        you did, for decades, so we could grow up amongst family and friends <span class="dot">•</span> my dry sense of humor,<br>
        I cherish it <span class="dot">•</span> finding a way, by hook or by crook, to send three children to college at the same time <span class="dot">•</span> never<br>
        giving up on trying to convince me that imperfection is not a failure <span class="dot">•</span> teaching me to try to find the good<br>
        in everyone <span class="dot">•</span> showing me that there is peace to be found in stillness and quiet <span class="dot">•</span> demonstrating the fun<br>
        that can be had and the truths that can be gleaned from debate <span class="dot">•</span> accepting me for who I am, no matter<br>
        who I love, and for helping me to accept myself <span class="dot">•</span> doing whatever you can to help whoever you can,<br>
        whether friend, family or stranger <span class="dot">•</span> trusting me enough to let your guard down<br>
        to let me know how you are truly doing <span class="dot">•</span> insisting, year after year,<br>
        that time with you means more than any<br>
        gift I could ever purchase
      </p>

      <svg class="waves" viewBox="0 0 657 130" aria-hidden="true">
        <path d="M0 28 C 120 8, 240 12, 360 30 S 560 60, 657 40" fill="none" stroke="var(--wave-blue)" stroke-width="4" opacity=".85"/>
        <path d="M0 34 C 130 14, 250 20, 370 38 S 570 62, 657 46" fill="none" stroke="var(--wave-light)" stroke-width="1.5" opacity=".8"/>
        <path d="M0 92 C 150 72, 300 78, 430 92 S 600 104, 657 90" fill="none" stroke="var(--wave-blue)" stroke-width="2" opacity=".8"/>
        <path d="M60 98 C 200 82, 330 88, 460 98 S 620 106, 657 96" fill="none" stroke="var(--wave-light)" stroke-width="1.2" opacity=".7"/>
      </svg>

      <p class="lesson">That is one lesson, amongst so many, that I will pass down to our next generation.</p>

      <div class="photo-scene" role="img" aria-label="Photograph: silhouette of a father and young son walking hand in hand through tall grass under a clear sky"></div>
    </main>
  </div>
</body>
</html>
```